Graphics for Vorlani telehealth weight loss plans

Vorlani focuses on delivering medical weight-loss using prescription medicine and telehealth consults. Vorlani needs graphics for its ecommerce site for three weight loss plans. The plans are posted here with current graphics and descriptions of what is included with each plan. Please do not feel constrained by current graphics or styling.

- https://shop.vorlanicare.com/products/steady-horizon-plan
- https://shop.vorlanicare.com/products/amber-ridge-plan
- https://shop.vorlanicare.com/products/calm-harbor-plan

The graphics need to look good on mobile and desktop browsers.

```html
<!DOCTYPE html>
<html lang="en">
<head>
<meta charset="utf-8">
<title>Vorlani Weight Loss Plans</title>
<link rel="stylesheet" href="https://fonts.googleapis.com/css2?family=Anton&family=Roboto:wght@400&display=swap">
<style>
  :root {
    --canvas: #333333;
    --ink: #1f1f1f;
    --icon: #1c1c1c;
    --rule: rgba(255,255,255,0.75);
    --sun-head: #fde60a;
    --sun-row-1: #fef8c9;
    --sun-row-2: #fdf4b0;
    --sun-row-3: #fcf098;
    --sun-row-4: #fbec82;
    --sun-row-5: #fbe970;
    --sun-art-a: #f4d3a6;
    --sun-art-b: #e6c2b0;
    --leaf-head: #94ad02;
    --leaf-row-1: #eaf0cc;
    --leaf-row-2: #d3df9b;
    --leaf-art-a: #e8c785;
    --leaf-art-b: #d9ccc0;
    --sea-head: #07e0f8;
    --sea-row-1: #cff7fd;
    --sea-row-2: #b6f4fb;
    --sea-row-3: #9cf1fa;
    --sea-row-4: #80edfa;
    --sea-art-a: #3b5f8f;
    --sea-art-b: #f2f4f7;
  }
  * { box-sizing: border-box; margin: 0; padding: 0; }
  html, body { width: 1200px; height: 1200px; overflow: hidden; background: var(--canvas); }
  .canvas { position: relative; width: 1200px; height: 1200px; }
  .plan-card {
    position: absolute; width: 396px; height: 555px;
    display: flex; flex-direction: column;
    box-shadow: 0 4px 14px rgba(0,0,0,0.35);
    font-family: "Roboto", Arial, sans-serif; color: var(--ink);
  }
  .plan-card--steady { left: 402px; top: 37px; }
  .plan-card--amber { left: 187px; top: 616px; }
  .plan-card--calm { left: 617px; top: 616px; }
  .plan-header { position: relative; border-bottom: 1px solid #2a2a2a; flex: none; }
  .plan-card--steady .plan-header { height: 212px; background: var(--sun-head); }
  .plan-card--amber .plan-header { height: 258px; background: var(--leaf-head); }
  .plan-card--calm .plan-header { height: 238px; background: var(--sea-head); }
  .plan-art { position: absolute; border-radius: 18px; }
  .plan-card--steady .plan-art { left: 20px; top: 16px; width: 182px; height: 186px;
    background: radial-gradient(ellipse at 50% 70%, var(--sun-art-b), var(--sun-art-a) 60%, rgba(244,211,166,0) 75%); }
  .plan-card--amber .plan-art { left: 15px; top: 27px; width: 205px; height: 208px;
    background: radial-gradient(ellipse at 45% 55%, var(--leaf-art-b), var(--leaf-art-a) 55%, rgba(232,199,133,0) 75%); }
  .plan-card--calm .plan-art { left: 14px; top: 36px; width: 227px; height: 164px;
    background: radial-gradient(ellipse at 50% 55%, var(--sea-art-b), var(--sea-art-a) 50%, rgba(59,95,143,0) 76%); }
  .plan-title {
    position: absolute; top: 0; bottom: 0; display: flex; align-items: center; justify-content: center;
    font-family: "Anton", "Oswald", Impact, sans-serif; font-weight: 400;
    font-size: 31px; line-height: 33px; text-align: center; color: #1d1d1d; letter-spacing: 0.3px;
  }
  .plan-card--steady .plan-title { left: 206px; width: 180px; padding-top: 6px; }
  .plan-card--amber .plan-title { left: 228px; width: 160px; padding-top: 6px; }
  .plan-card--calm .plan-title { left: 238px; width: 158px; padding-top: 4px; }
  .feature-list { list-style: none; flex: 1; display: flex; flex-direction: column; }
  .feature {
    flex: 1; display: flex; align-items: center; gap: 13px;
    padding: 0 14px 0 18px; font-size: 15.6px; line-height: 24px;
    border-top: 2px solid var(--rule);
  }
  .feature:first-child { border-top: none; }
  .feature-icon { width: 40px; height: 42px; flex: none; }
  .plan-card--steady .feature:nth-child(1) { background: var(--sun-row-1); }
  .plan-card--steady .feature:nth-child(2) { background: var(--sun-row-2); }
  .plan-card--steady .feature:nth-child(3) { background: var(--sun-row-3); }
  .plan-card--steady .feature:nth-child(4) { background: var(--sun-row-4); }
  .plan-card--steady .feature:nth-child(5) { background: var(--sun-row-5); }
  .plan-card--amber .feature { flex-direction: column; justify-content: center; gap: 18px; text-align: center; padding: 0 14px; }
  .plan-card--amber .feature:nth-child(1) { background: var(--leaf-row-1); }
  .plan-card--amber .feature:nth-child(2) { background: var(--leaf-row-2); }
  .plan-card--calm .feature { padding-left: 17px; gap: 14px; }
  .plan-card--calm .feature:nth-child(1) { background: var(--sea-row-1); }
  .plan-card--calm .feature:nth-child(2) { background: var(--sea-row-2); }
  .plan-card--calm .feature:nth-child(3) { background: var(--sea-row-3); }
  .plan-card--calm .feature:nth-child(4) { background: var(--sea-row-4); }
</style>
</head>
<body>
<svg width="0" height="0" style="position:absolute" aria-hidden="true">
  <defs>
    <path id="hex-badge" d="M15 2.5 Q20 0 25 2.5 L34.5 8 Q39 10.5 39 15.5 L39 26.5 Q39 31.5 34.5 34 L25 39.5 Q20 42 15 39.5 L5.5 34 Q1 31.5 1 26.5 L1 15.5 Q1 10.5 5.5 8 Z" fill="#1c1c1c"/>
    <g id="icon-physician">
      <use href="#hex-badge"/>
      <circle cx="16" cy="15" r="4" fill="none" stroke="#fff" stroke-width="1.5"/>
      <path d="M9 30 Q9 21 16 21 Q23 21 23 30" fill="none" stroke="#fff" stroke-width="1.5"/>
      <rect x="23" y="13" width="9" height="9" rx="1.5" fill="#fff"/>
      <path d="M27.5 14.5 v6 M24.5 17.5 h6" stroke="#1c1c1c" stroke-width="1.6"/>
    </g>
    <g id="icon-nutrition">
      <use href="#hex-badge"/>
      <path d="M10 22 h14 l-2 8 h-10 z" fill="#fff"/>
      <circle cx="13" cy="20" r="2" fill="#fff"/><circle cx="17" cy="19" r="2" fill="#fff"/><circle cx="21" cy="20" r="2" fill="#fff"/>
      <path d="M12 16 Q12 11 16 11 Q16 15 12 16" fill="#fff"/>
      <circle cx="27" cy="14" r="3" fill="none" stroke="#fff" stroke-width="1.4"/>
      <path d="M22 27 Q22 20 27 20 Q32 20 32 27" fill="none" stroke="#fff" stroke-width="1.4"/>
    </g>
    <g id="icon-diet">
      <use href="#hex-badge"/>
      <rect x="11" y="11" width="15" height="20" rx="1.5" fill="none" stroke="#fff" stroke-width="1.5"/>
      <path d="M14 16 h9 M14 20 h9 M14 24 h6" stroke="#fff" stroke-width="1.4"/>
      <circle cx="27" cy="27" r="4" fill="#fff"/>
      <path d="M27 23 q1 -3 3 -3" stroke="#fff" stroke-width="1.2" fill="none"/>
    </g>
    <g id="icon-coaching">
      <use href="#hex-badge"/>
      <circle cx="20" cy="13" r="3" fill="none" stroke="#fff" stroke-width="1.4"/>
      <path d="M20 17 v14 M16 31 h8" stroke="#fff" stroke-width="1.5"/>
      <path d="M10 20 h6 M10 24 h6 M10 28 h6 M24 20 h6 M24 24 h6 M24 28 h6" stroke="#fff" stroke-width="1.3"/>
    </g>
    <g id="icon-payment">
      <use href="#hex-badge"/>
      <circle cx="23" cy="21" r="7.5" fill="none" stroke="#fff" stroke-width="1.6"/>
      <path d="M25.5 17.5 Q23 16 21 17.5 Q19.8 19.5 23 20.8 Q26.2 22 25 24.5 Q23 26 20.5 24.5 M23 15 v12" fill="none" stroke="#fff" stroke-width="1.4"/>
      <path d="M8 17 h5 M7 21 h6 M8 25 h5" stroke="#fff" stroke-width="1.5" stroke-linecap="round"/>
    </g>
  </defs>
</svg>

<main class="canvas">
  <article class="plan-card plan-card--steady">
    <header class="plan-header">
      <div class="plan-art" role="img" aria-label="Illustration of a woman with a medical chart, capsules and a plate of healthy foods"></div>
      <h2 class="plan-title">Steady<br>Horizon<br>Plan</h2>
    </header>
    <ul class="feature-list">
      <li class="feature"><svg class="feature-icon" viewBox="0 0 40 42" aria-hidden="true"><use href="#icon-physician"/></svg><span>Physician Consultation Phentermine Program</span></li>
      <li class="feature"><svg class="feature-icon" viewBox="0 0 40 42" aria-hidden="true"><use href="#icon-nutrition"/></svg><span>Expert Nutrition Consult</span></li>
      <li class="feature"><svg class="feature-icon" viewBox="0 0 40 42" aria-hidden="true"><use href="#icon-diet"/></svg><span>Custom Crafted Diet Plan To Achieve<br>Your Goals</span></li>
      <li class="feature"><svg class="feature-icon" viewBox="0 0 40 42" aria-hidden="true"><use href="#icon-coaching"/></svg><span>Nutritionist Coaching To Improve Your Health<br>And Vitality</span></li>
      <li class="feature"><svg class="feature-icon" viewBox="0 0 40 42" aria-hidden="true"><use href="#icon-payment"/></svg><span>Month-To-Month Pay As You Go</span></li>
    </ul>
  </article>

  <article class="plan-card plan-card--amber">
    <header class="plan-header">
      <div class="plan-art" role="img" aria-label="Illustration of a man on a laptop in an armchair beside a prescription sheet and a jar of capsules"></div>
      <h2 class="plan-title">Amber<br>Ridge<br>Plan</h2>
    </header>
    <ul class="feature-list">
      <li class="feature"><svg class="feature-icon" viewBox="0 0 40 42" aria-hidden="true"><use href="#icon-physician"/></svg><span>Physician Consultation Phentermine Program</span></li>
      <li class="feature"><svg class="feature-icon" viewBox="0 0 40 42" aria-hidden="true"><use href="#icon-payment"/></svg><span>Month-To-Month Pay As You Go</span></li>
    </ul>
  </article>

  <article class="plan-card plan-card--calm">
    <header class="plan-header">
      <div class="plan-art" role="img" aria-label="Illustration of a nutritionist on a laptop screen with a food chart, fruit and a dumbbell"></div>
      <h2 class="plan-title">Calm<br>Harbor<br>Plan</h2>
    </header>
    <ul class="feature-list">
      <li class="feature"><svg class="feature-icon" viewBox="0 0 40 42" aria-hidden="true"><use href="#icon-nutrition"/></svg><span>Expert Nutrition Consult</span></li>
      <li class="feature"><svg class="feature-icon" viewBox="0 0 40 42" aria-hidden="true"><use href="#icon-diet"/></svg><span>Custom Crafted Diet Plan To Achieve<br>Your Goals</span></li>
      <li class="feature"><svg class="feature-icon" viewBox="0 0 40 42" aria-hidden="true"><use href="#icon-coaching"/></svg><span>Nutritionist Coaching To Improve Your Health<br>And Vitality</span></li>
      <li class="feature"><svg class="feature-icon" viewBox="0 0 40 42" aria-hidden="true"><use href="#icon-payment"/></svg><span>Month-To-Month Pay As You Go</span></li>
    </ul>
  </article>
</main>
</body>
</html>
```